依頼詳細
PC版のTOPページと下層1ページ(採用情報)のデザイン制作をお願いいたします。
サイトマップ、依頼内容詳細.txtをご確認いただき、動画のテイストを参考にシンプルで見やすいデザインで制作いただきたいです。
スムーズな連絡と軽微な修正にご対応いただける方へご依頼をさせていただきたいです。
ターゲットは木材資材・建築資材・家具建具資材などを必要とする建築会社様、家具・建具製造会社様などです。
ページ数
2ページ
希望イメージ
シンプル 複雑
単色 カラフル
暗い 明るい
日常 高級
遊び心 厳粛
未来的 伝統的
女性的 男性的
希望する色
茶系、緑系、グレー系
納品ファイル
• イラストレーター形式 (.ai)
補足説明
納品ファイルはXDも可です。
添付してあるアニメーションにテイストを合わせ、
木の温かみを感じさせるデザインで制作してください。
コーポレートですが、あまり堅くなり過ぎないようにしたいです。
BtoB向けの会社ではありますが、就職などを考えている若い方が見ても、
面白そうな企業だなという印象も与えたいです。
動画ダウンロードURLを新たに添付いたしましたので
そちらからダウンロードをお願い致します。
■ 選んだ理由

爽やかな緑を使ったデザインが良かったです。

■ 提案者全員のお礼・コメント

たくさんのご提案をいただきありがとうございました。

```html
<!DOCTYPE html>
<html lang="ja">
<head>
<meta charset="utf-8">
<title>KITAMORI TIMBER WORKS</title>
<link href="https://fonts.googleapis.com/css2?family=Roboto:wght@400;500;700&family=Noto+Sans+JP:wght@400;500;700&display=swap" rel="stylesheet">
<style>
:root{
  --green:#2e8b2e;
  --leaf-soft:#e3f0dc;
  --leaf-mid:#cfe4c4;
  --brown:#6b3a1a;
  --ink:#222;
  --muted:#666;
  --grey-bg:#f4f4f4;
  --cream:#fdf4e8;
  --white:#fff;
}
*{margin:0;padding:0;box-sizing:border-box}
html,body{width:1200px;height:3372px;overflow:hidden}
body{font-family:"Noto Sans JP",sans-serif;color:var(--ink);background:var(--white);position:relative}
.abs{position:absolute}

/* header */
.site-header{position:absolute;left:0;top:0;width:1200px;height:60px}
.brand{position:absolute;left:20px;top:14px}
.brand-name{font-family:"Roboto",sans-serif;font-weight:500;font-size:20px;letter-spacing:.5px}
.brand-sub{font-size:9px;color:var(--muted);margin-top:2px}
.global-nav{position:absolute;right:24px;top:20px;display:flex;gap:22px;font-size:11px}

/* hero */
.hero{position:absolute;left:4px;top:64px;width:1192px;height:680px;border:8px solid var(--green);background:var(--white)}
.hero-art{position:absolute;background:linear-gradient(180deg,var(--leaf-mid),var(--leaf-soft))}
.hero-art-left{left:24px;top:40px;width:300px;height:300px}
.hero-art-right{right:24px;top:20px;width:280px;height:320px}
.hero-title{position:absolute;left:0;top:380px;width:100%;text-align:center;font-family:"Roboto",sans-serif;font-weight:500;font-size:92px;line-height:118px;letter-spacing:4px;color:#111}

/* common */
.sec-title{font-family:"Roboto",sans-serif;font-weight:500;font-size:58px;line-height:1}
.sec-sub{font-size:10px;color:var(--muted);margin-top:6px}
.body-text{font-size:11px;line-height:20px;color:#333}
.btn{display:inline-block;width:130px;height:38px;line-height:38px;background:var(--brown);color:var(--white);font-size:11px;text-align:center}
.photo{position:absolute}

/* message */
.message-photo{left:0;top:800px;width:600px;height:360px;background:linear-gradient(135deg,#f3e9dc,#c99a66 70%,#8a5a32)}
.message-body{left:640px;top:840px;width:520px}

/* news */
.news{position:absolute;left:0;top:1200px;width:1200px;height:240px;background:var(--grey-bg)}
.news-head{position:absolute;left:222px;top:64px}
.news-list{position:absolute;left:460px;top:86px;list-style:none;font-size:10px;color:#444}
.news-list li{height:50px;display:flex;gap:28px}

/* service */
.service-photo{left:0;top:1520px;width:1200px;height:440px;background:linear-gradient(180deg,#e6c39a,#c8925a 50%,#9a6536)}
.service-card{position:absolute;left:460px;top:1520px;width:280px;height:220px;background:var(--white);text-align:center;padding-top:18px}

/* products */
.products{position:absolute;left:0;top:1990px;width:1200px;height:440px;background:var(--cream)}
.products-body{position:absolute;left:220px;top:70px;width:230px}
.wood-grid{position:absolute;left:525px;top:60px;width:385px;height:320px;display:grid;grid-template-columns:1fr 1fr;grid-template-rows:1fr 1fr}
.wood-a{background:linear-gradient(135deg,#e9c99e,#d6a66c)}
.wood-b{background:linear-gradient(135deg,#f0d9b8,#e2bf92)}
.wood-c{background:linear-gradient(135deg,#ead6bd,#d8b891)}
.wood-d{background:linear-gradient(135deg,#f3e6d3,#e4ceb0)}

/* recruit */
.recruit-photo{left:0;top:2470px;width:600px;height:310px;background:linear-gradient(135deg,#dfe7ef,#9fb1c4 55%,#3c4a5c)}
.recruit-body{left:640px;top:2500px;width:520px}

/* contact */
.contact{position:absolute;left:0;top:2890px;width:1200px;height:300px;background:linear-gradient(180deg,#6c6c6c,#3b3b3b)}
.contact-title{position:absolute;left:0;top:44px;width:100%;text-align:center;color:var(--white)}
.contact-title .sec-sub{color:#ddd}
.contact-btn{position:absolute;top:154px;height:70px;border:2px solid var(--white);border-radius:6px;color:var(--white);display:flex;align-items:center;justify-content:center;gap:14px}
.contact-tel{left:290px;width:270px;font-family:"Roboto",sans-serif;font-size:30px}
.contact-mail{left:660px;width:250px;font-size:24px}

/* footer */
.site-footer{position:absolute;left:0;top:3190px;width:1200px;height:182px;background:var(--white)}
.footer-brand{position:absolute;left:238px;top:42px}
.footer-info{font-size:9px;color:var(--muted);line-height:16px;margin-top:8px}
.footer-links{position:absolute;top:42px;list-style:none;font-size:9px;color:#444;line-height:22px}
</style>
</head>
<body>

<header class="site-header">
  <div class="brand">
    <div class="brand-name">KITAMORI TIMBER WORKS</div>
    <div class="brand-sub">北森木材株式会社</div>
  </div>
  <nav class="global-nav">
    <span>会社概要</span><span>事業内容</span><span>製品情報</span><span>採用情報</span><span>お問い合わせ</span>
  </nav>
</header>

<section class="hero">
  <div class="hero-art hero-art-left" role="img" aria-label="実のなる緑の木のイラスト"></div>
  <div class="hero-art hero-art-right" role="img" aria-label="緑の葉が茂る木のイラスト"></div>
  <h1 class="hero-title">KITAMORI<br>TIMBER WORKS</h1>
</section>

<div class="photo message-photo" role="img" aria-label="木の床と家具が並ぶ明るいリビングの写真"></div>
<section class="abs message-body">
  <h2 class="sec-title">Message</h2>
  <p class="sec-sub">ご挨拶</p>
  <p class="body-text" style="margin-top:22px">北森木材株式会社は、創業以来、木材の調達と加工を通じて地域の住まいづくりを支えてきました。<br>お客様の声に寄り添い、確かな品質の木材をお届けしています。<br>木の温もりを、次の世代へ。</p>
  <a class="btn" style="margin-top:26px">会社概要</a>
</section>

<section class="news">
  <div class="news-head">
    <h2 class="sec-title">News</h2>
    <p class="sec-sub">お知らせ</p>
    <a class="btn" style="margin-top:20px;width:120px;height:30px;line-height:30px">お知らせ一覧</a>
  </div>
  <ul class="news-list">
    <li><span>2021.00.00</span><span>新しい製品ラインナップを公開しました。詳しくは製品情報をご覧ください。</span></li>
    <li><span>2021.00.00</span><span>夏季休業期間のお知らせ。期間中のお問い合わせは休業明けに対応します。</span></li>
    <li><span>2021.00.00</span><span>採用情報を更新しました。新卒・中途ともに募集を行っています。</span></li>
  </ul>
</section>

<div class="photo service-photo" role="img" aria-label="積み上げられた製材の写真"></div>
<section class="service-card">
  <h2 class="sec-title">Service</h2>
  <p class="sec-sub">事業内容</p>
  <p class="body-text" style="margin-top:14px">建築用材・家具用材・建具用材の販売<br>プレカット加工・乾燥処理・輸入木材の取扱い</p>
  <a class="btn" style="margin-top:14px;width:110px;height:30px;line-height:30px">事業内容</a>
</section>

<section class="products">
  <div class="products-body">
    <h2 class="sec-title">Products</h2>
    <p class="sec-sub">製品情報</p>
    <p class="body-text" style="margin-top:18px">国産材から輸入材まで、用途に合わせた多彩な木材を取り揃えています。無垢材・集成材・合板など、品質にこだわった製品をご提案します。</p>
    <a class="btn" style="margin-top:18px;width:110px;height:30px;line-height:30px">製品情報</a>
  </div>
  <div class="wood-grid">
    <div class="wood-a" role="img" aria-label="明るい木目の板材"></div>
    <div class="wood-b" role="img" aria-label="淡い色の木目の板材"></div>
    <div class="wood-c" role="img" aria-label="節のある木目の板材"></div>
    <div class="wood-d" role="img" aria-label="白っぽい木目の板材"></div>
  </div>
</section>

<div class="photo recruit-photo" role="img" aria-label="書類を手に話す社員たちの写真"></div>
<section class="abs recruit-body">
  <h2 class="sec-title">Recruit</h2>
  <p class="sec-sub">採用情報</p>
  <p class="body-text" style="margin-top:22px">木に関わる仕事で、一緒に未来をつくる仲間を募集しています。</p>
  <a class="btn" style="margin-top:40px">採用情報</a>
</section>

<section class="contact" role="img" aria-label="オフィスビルの外観写真を背景にしたお問い合わせ欄">
  <div class="contact-title">
    <h2 class="sec-title">Contact</h2>
    <p class="sec-sub">お問い合わせ</p>
  </div>
  <div class="contact-btn contact-tel">
    <svg width="26" height="26" viewBox="0 0 24 24" fill="none" stroke="#fff" stroke-width="2"><path d="M5 3h4l2 5-3 2a11 11 0 0 0 6 6l2-3 5 2v4a2 2 0 0 1-2 2A17 17 0 0 1 3 5a2 2 0 0 1 2-2z"/></svg>
    <span>011-555-0148</span>
  </div>
  <div class="contact-btn contact-mail">
    <svg width="28" height="22" viewBox="0 0 28 22" fill="none" stroke="#fff" stroke-width="2"><rect x="1" y="1" width="26" height="20"/><path d="M1 1l13 11L27 1"/></svg>
    <span>メールフォーム</span>
  </div>
</section>

<footer class="site-footer">
  <div class="footer-brand">
    <div class="brand-name">KITAMORI TIMBER WORKS</div>
    <div class="brand-sub">北森木材株式会社</div>
    <p class="footer-info">〒000-0000 北海道札幌市中央区1-2-3<br>TEL 011-555-0148 FAX 011-555-0149</p>
  </div>
  <ul class="footer-links" style="left:780px"><li>ホーム</li><li>会社概要</li><li>事業内容</li><li>製品情報</li></ul>
  <ul class="footer-links" style="left:900px"><li>採用情報</li><li>お知らせ</li><li>お問い合わせ</li><li>プライバシーポリシー</li></ul>
</footer>

</body>
</html>
```